We need a new design for our construction website

We need a new website for our wordpress site ferncrestworks.co.nz

It needs to be only a few pages but sleek in design and responsive, beautifully showcasing our images and video. Currently we have
1. home
2. about us
3. contact
We need either a front page that is designed much better to showcase more content, or potentially a projects page which has images from our builds. We don't have a lot of content so the content we do have needs to be maximised by image, rather than project.

Target Market(s)

High end residential construction and renovation projects, people wanting to build a nice home, clients based in Mount Maunganui, Tauranga.

Coding

Font styles to use
Sans Serif

Colors

Designer to choose only greyscale colors for use in the design.

Requirements
Must have
• A sleek design, architectural

```html
<!DOCTYPE html>
<html lang="en">
<head>
<meta charset="utf-8">
<title>Ferncrest — Construction</title>
<link href="https://fonts.googleapis.com/css2?family=Montserrat:wght@300;400;500&display=swap" rel="stylesheet">
<style>
:root{
  --white:#ffffff;
  --ink:#1c1c1c;
  --text:#3a3a3a;
  --muted:#6b6b6b;
  --line:#cfcfcf;
  --accent:#e7ac12;
  --footer:#050505;
  --dark-band:#2a231d;
}
*{margin:0;padding:0;box-sizing:border-box}
html,body{width:1200px;height:3702px;overflow:hidden}
body{position:relative;background:var(--white);font-family:"Montserrat",Arial,sans-serif;color:var(--text);font-weight:300}
.abs{position:absolute}

/* Hero */
.hero{left:0;top:0;width:1200px;height:637px;
  background:linear-gradient(180deg,#3f4650 0%,#5a5246 35%,#7a5a30 60%,#3d4a3a 82%,#3f8fb8 100%)}
.hero-shade{left:0;top:0;width:1200px;height:637px;background:linear-gradient(90deg,rgba(0,0,0,.35),rgba(0,0,0,0) 60%)}
.brand{left:89px;top:34px;display:flex;align-items:center;gap:14px;color:var(--white);font-weight:400;font-size:24px;letter-spacing:11px}
.brand-square{width:30px;height:30px;border:2px solid var(--white)}
.phone{left:952px;top:17px;color:var(--white);font-size:19px;font-weight:400;display:flex;align-items:center;gap:10px}
.nav{top:62px;font-size:16px;color:var(--white)}
.nav.active{color:var(--accent)}
.hero-title{left:168px;top:215px;color:var(--white);font-size:64px;font-weight:300;letter-spacing:6px}
.hero-text{left:170px;top:302px;color:var(--white);font-size:20px;line-height:28px}
.hero-link{left:171px;top:384px;color:var(--white);font-size:16px;text-decoration:underline;display:flex;gap:10px;align-items:center}
.social-dot{left:42px;top:566px;width:12px;height:12px;border-radius:50%;background:var(--white)}

/* Section labels */
.label{font-size:13px;font-weight:400;color:var(--ink);display:flex;align-items:center;gap:8px}
.label::before{content:"";width:64px;border-top:1px dotted #999}
.label.light{color:var(--white)}
.heading{font-size:42px;font-weight:300;color:var(--ink)}
.heading.light{color:var(--white)}

/* Service cards */
.card{top:823px;width:292px;height:338px;border-radius:4px;overflow:hidden}
.card-shade{position:absolute;inset:0;background:linear-gradient(180deg,rgba(0,0,0,0) 55%,rgba(0,0,0,.7))}
.card-num{position:absolute;left:16px;top:240px;color:var(--white);font-size:22px;font-weight:500}
.card-text{position:absolute;left:16px;top:282px;color:var(--white);font-size:16px;line-height:23px;font-weight:400}

/* Why band */
.why{left:0;top:1262px;width:1200px;height:488px;background:linear-gradient(120deg,#1d1915,#3a2e22 45%,#2b241c 70%,#1a1612)}
.why-shade{left:0;top:1262px;width:1200px;height:488px;background:rgba(0,0,0,.35)}
.feature-title{color:var(--white);font-size:18px;font-weight:400;line-height:23px}
.feature-text{color:var(--white);font-size:13px;line-height:25px}
.feature-arrow{color:var(--white);font-size:18px}

/* Vision */
.vision-text{left:144px;top:1938px;font-size:22px;line-height:36px;color:var(--ink);font-weight:400}
.tile{width:394px;height:468px;border-radius:3px;overflow:hidden}
.tile-caption{position:absolute;left:0;bottom:0;width:256px;height:127px;background:var(--white);padding:22px 14px}
.tile-caption h3{color:var(--accent);font-size:18px;font-weight:400;margin-bottom:14px}
.tile-caption p{font-size:15px;line-height:24px;color:var(--text)}

.news-text{left:663px;top:3204px;font-size:23px;line-height:32px;color:var(--ink);font-weight:400}
.news-field{left:663px;top:3308px;width:394px;height:34px;border-bottom:1px solid var(--line);font-size:15px;color:var(--ink);font-weight:400;display:flex;justify-content:space-between;align-items:center}

/* Footer */
.footer{left:0;top:3434px;width:1200px;height:268px;background:var(--footer);color:var(--white);text-align:center}
.footer-brand{position:absolute;left:0;width:1200px;top:66px;display:flex;justify-content:center;align-items:center;gap:18px;font-size:29px;letter-spacing:16px;font-weight:400}
.footer-brand .brand-square{width:36px;height:36px}
.footer-line{position:absolute;left:0;width:1200px;font-size:14px;font-weight:400;display:flex;justify-content:center;gap:12px;align-items:center}
</style>
</head>
<body>

<!-- Hero -->
<div class="abs hero" role="img" aria-label="Modern two-storey home with solar panel roof and lit windows beside a pool at dusk"></div>
<div class="abs hero-shade"></div>
<div class="abs brand"><span class="brand-square"></span>FERNCREST</div>
<div class="abs phone">
  <svg width="18" height="18" viewBox="0 0 24 24" fill="none" stroke="#fff" stroke-width="1.8"><path d="M5 3h4l2 5-2.5 1.5a11 11 0 0 0 6 6L16 13l5 2v4a2 2 0 0 1-2 2A17 17 0 0 1 3 5a2 2 0 0 1 2-2z"/></svg>
  0270 418 263
</div>
<div class="abs nav active" style="left:684px">Home</div>
<div class="abs nav" style="left:780px">About</div>
<div class="abs nav" style="left:878px">Gallery</div>
<div class="abs nav" style="left:981px">Contact</div>
<svg class="abs" style="left:1094px;top:65px" width="15" height="15" viewBox="0 0 16 16" fill="none" stroke="#fff" stroke-width="2"><circle cx="6.5" cy="6.5" r="4.5"/><path d="M10 10l4.5 4.5"/></svg>

<h1 class="abs hero-title">FERNCREST</h1>
<p class="abs hero-text">Lorem ipsum dolor sit amet, consectetur adipiscing elit,<br>sed do eiusmod tempor incididunt utariatur.</p>
<div class="abs hero-link">Get Started
  <svg width="12" height="12" viewBox="0 0 12 12" fill="#fff"><path d="M5 1l5 5-5 5-1.2-1.2L6.6 7H1V5h5.6L3.8 2.2z"/></svg>
</div>
<span class="abs social-dot"></span>
<svg class="abs" style="left:170px;top:564px" width="28" height="16" viewBox="0 0 28 16" fill="none" stroke="#fff" stroke-width="2"><path d="M2 2l12 11L26 2"/></svg>

<!-- What we do -->
<div class="abs label" style="left:144px;top:725px">What We Do</div>
<h2 class="abs heading" style="left:142px;top:752px">We Create</h2>

<div class="abs card" style="left:144px;background:linear-gradient(160deg,#6d6458,#a88456 55%,#5c4a36)" role="img" aria-label="Modern kitchen with timber island and bar stools">
  <div class="card-shade"></div><div class="card-num">01.</div>
  <div class="card-text">Residential Construction<br>For Mount Maunganui,Tauranga</div>
</div>
<div class="abs card" style="left:454px;background:linear-gradient(160deg,#c9b8a0,#e0d6c8 45%,#8a5a3a)" role="img" aria-label="Renovated hallway with timber batten screen and staircase">
  <div class="card-shade"></div><div class="card-num">02.</div>
  <div class="card-text">Renovation Projects<br>For Mount Maunganui,Tauranga</div>
</div>
<div class="abs card" style="left:764px;background:linear-gradient(160deg,#8a6a46,#7c8a6a 45%,#c9c4bc)" role="img" aria-label="Bedroom with timber ceiling and large window to green hills">
  <div class="card-shade"></div><div class="card-num">03.</div>
  <div class="card-text">Build a Nice Home<br>For Mount Maunganui,Tauranga</div>
</div>

<!-- Why choose us -->
<div class="abs why" role="img" aria-label="Builders standing inside a timber house frame under construction"></div>
<div class="abs why-shade"></div>
<div class="abs label light" style="left:144px;top:1336px">Why Us</div>
<h2 class="abs heading light" style="left:142px;top:1362px">Why Choose Us</h2>

<svg class="abs" style="left:144px;top:1453px" width="36" height="38" viewBox="0 0 36 38" fill="none" stroke="var(--accent)" stroke-width="2"><path d="M3 17L18 3l15 14M7 14v21h22V14M14 35V24h8v11"/></svg>
<svg class="abs" style="left:375px;top:1453px" width="40" height="38" viewBox="0 0 40 38" fill="none" stroke="var(--accent)" stroke-width="2"><path d="M6 4l28 30M3 7l4-4 4 3-3 4zM34 4a6 6 0 0 0-8 8L6 32l3 3 20-20a6 6 0 0 0 8-8l-4 3-3-2z"/></svg>
<svg class="abs" style="left:617px;top:1453px" width="38" height="38" viewBox="0 0 38 38" fill="none" stroke="var(--accent)" stroke-width="2"><path d="M20 6H4v30h30V20M30 3l5 5-16 16-7 2 2-7z"/></svg>
<svg class="abs" style="left:892px;top:1450px" width="30" height="44" viewBox="0 0 30 44" fill="none" stroke="var(--accent)" stroke-width="2"><path d="M15 2a12 12 0 0 0-7 22c2 2 2 4 2 7h10c0-3 0-5 2-7A12 12 0 0 0 15 2zM10 35h10M11 40h8"/></svg>

<div class="abs" style="left:142px;top:1522px;width:200px">
  <div class="feature-title">Design and Build</div>
  <p class="feature-text" style="margin-top:10px">The Design and Build<br>process streamlines your<br>home construction</p>
  <div class="feature-arrow" style="margin-top:4px">⟶</div>
</div>
<div class="abs" style="left:375px;top:1522px;width:200px">
  <div class="feature-title">Renovations &amp;<br>Additions</div>
  <p class="feature-text" style="margin-top:10px">Improving the layout and<br>functionality of your home<br>doesn't mean having to</p>
  <div class="feature-arrow" style="margin-top:4px">⟶</div>
</div>
<div class="abs" style="left:616px;top:1522px;width:240px">
  <div class="feature-title">Project Management</div>
  <p class="feature-text" style="margin-top:10px">We specialise in managing<br>your entire build project. From<br>liaising with your designer</p>
  <div class="feature-arrow" style="margin-top:4px">⟶</div>
</div>
<div class="abs" style="left:888px;top:1522px;width:220px">
  <div class="feature-title">Build Smarter</div>
  <p class="feature-text" style="margin-top:10px">We are passionate about<br>building smarter, even better<br>than the building code.</p>
  <div class="feature-arrow" style="margin-top:4px">⟶</div>
</div>

<!-- Vision -->
<div class="abs label" style="left:144px;top:1843px">Vision</div>
<h2 class="abs heading" style="left:142px;top:1870px">Our Vision</h2>
<p class="abs vision-text">Build beautiful, efficient homes<br>with the best building technologies<br>available that our customers are<br>proud to own</p>

<div class="abs tile" style="left:662px;top:1847px;background:linear-gradient(180deg,#dcdcdc 0%,#c8c8c8 25%,#4b4038 45%,#6b4a30 65%,#8a8a86 100%)" role="img" aria-label="New two-storey home with timber cladding and large gable windows">
  <div class="tile-caption"><h3>About Us</h3><p>Lorem ipsum dolor sit amet,<br>consectetur adipiscing</p></div>
</div>
<div class="abs tile" style="left:145px;top:2186px;background:linear-gradient(180deg,#3a6fc4 0%,#7fa6dc 35%,#3d4a3a 55%,#7a5048 75%,#3a3f6a 100%)" role="img" aria-label="Floor framing and reinforcing on a coastal building site under blue sky">
  <div class="tile-caption"><h3>Our Projects</h3><p>Lorem ipsum dolor sit amet,<br>consectetur adipiscing</p></div>
</div>
<div class="abs tile" style="left:662px;top:2528px;background:linear-gradient(180deg,#e8e4dc 0%,#d9b17a 20%,#c99a5e 60%,#e8e4e4 80%,#4a4a6a 100%)" role="img" aria-label="Bedroom with pine panelled walls, framed pictures and patterned cushions">
  <div class="tile-caption"><h3>Testimonials</h3><p>Lorem ipsum dolor sit amet,<br>consectetur adipiscing</p></div>
</div>
<div class="abs tile" style="left:145px;top:2870px;background:linear-gradient(180deg,#5a8ad0 0%,#b8cce6 22%,#1f1f22 40%,#2a2a2e 70%,#c9a97a 100%)" role="img" aria-label="Dark clad cabin with awning, sliding door and outdoor chairs on a deck">
  <div class="tile-caption"><h3>Newsletter</h3><p>We'd love to hear about your<br>building project and discuss</p></div>
</div>

<!-- Newsletter -->
<div class="abs label" style="left:663px;top:3106px">Get In Touch</div>
<h2 class="abs heading" style="left:661px;top:3132px">Join Our Newsletter</h2>
<p class="abs news-text">Contact us for a free no obligation<br>chat about your building project</p>
<div class="abs news-field"><span>Enter Your Email Address</span><span style="color:#999">⟶</span></div>

<!-- Footer -->
<footer class="abs footer">
  <div class="footer-brand"><span class="brand-square"></span>FERNCREST</div>
  <div class="footer-line" style="top:146px">
    <span>
      <svg width="10" height="13" viewBox="0 0 10 13" fill="#fff"><path d="M5 0a5 5 0 0 0-5 5c0 4 5 8 5 8s5-4 5-8a5 5 0 0 0-5-5zm0 7a2 2 0 1 1 0-4 2 2 0 0 1 0 4z"/></svg>
      18 Harbour View Road, Tauranga, NZ</span><span>|</span>
    <span>
      <svg width="12" height="12" viewBox="0 0 24 24" fill="#fff"><path d="M5 2h4l2 5-2.5 1.5a11 11 0 0 0 6 6L16 12l5 2v4a2 2 0 0 1-2 2A17 17 0 0 1 3 4a2 2 0 0 1 2-2z"/></svg>
      0270 418 263</span><span>|</span>
    <span>
      <svg width="13" height="10" viewBox="0 0 13 10" fill="#fff"><path d="M0 0h13v1.5L6.5 5.5 0 1.5zM0 3l6.5 4L13 3v7H0z"/></svg>
      admin@ferncrestworks.co.nz</span>
  </div>
  <div class="footer-line" style="top:185px;gap:22px">
    <span>Home</span><span>|</span><span>About Us</span><span>|</span><span>Gallery</span><span>|</span><span>Contact Us</span>
  </div>
  <div class="footer-line" style="top:220px">Copyrights © 2020, The Company Name. All rights reserved.</div>
</footer>

</body>
</html>
```